BPH Business Card 2018

Brellmore Chiropractic. We have two locations that we want to advertise on the same card. Calderwick OrthoAxis campus address: 3815 Pemberly Dr., Suite 240, Flowood, MS 39587. Madison address: 426 Larkmoor Dr., Building D., Madison, MS 39674. website: www.drbrellmore.example. o:(601)555-0148 f:(601)555-0173

Target Market(s)

Health care decision makers: primary care doctors and mothers

Contact Information for Business Card

I have no idea; up for any suggestions and I'd do much better picking from examples versus describing what I'm looking for. We are in a very high end location and would like the cards to look really sharp.

Requirements
Must have
• My name, Tobias R Venmark, D.C.

```html
<!DOCTYPE html>
<html lang="en">
<head>
<meta charset="utf-8">
<title>Brellmore Chiropractic – Business Card</title>
<link href="https://fonts.googleapis.com/css2?family=Cormorant+Garamond:wght@600&family=Work+Sans:wght@400;500&display=swap" rel="stylesheet">
<style>
  :root {
    --backdrop: #1c1c1d;
    --card: #141414;
    --card-edge: #262626;
    --ink: #f2f2f2;
    --ink-soft: #d6d6d6;
    --rule: #e8e8e8;
    --pattern-a: #1a1a1a;
    --pattern-b: #0e0e0e;
  }
  * { box-sizing: border-box; margin: 0; padding: 0; }
  html, body { width: 1200px; height: 900px; overflow: hidden; }
  body {
    background: var(--backdrop);
    display: flex;
    flex-direction: column;
    align-items: center;
    justify-content: center;
    gap: 40px;
  }
  .card {
    position: relative;
    width: 700px;
    height: 400px;
    background: var(--card);
    border: 1px solid var(--card-edge);
    box-shadow: 0 12px 30px rgba(0,0,0,.45);
    overflow: hidden;
  }

  /* Front */
  .card-front .pattern-field {
    position: absolute;
    inset: 0;
    background: radial-gradient(ellipse at 60% 40%, var(--pattern-a), var(--pattern-b));
  }
  .wordmark {
    font-family: "Cormorant Garamond", serif;
    font-weight: 600;
    color: var(--ink);
    line-height: 0.95;
  }
  .wordmark .name { display: block; letter-spacing: 0.02em; }
  .wordmark .trade { display: block; font-variant: small-caps; letter-spacing: 0.03em; }
  .card-front .wordmark {
    position: absolute;
    left: 125px;
    top: 150px;
  }
  .card-front .wordmark .name { font-size: 50px; }
  .card-front .wordmark .trade { font-size: 34px; }

  /* Back */
  .card-back .brand {
    position: absolute;
    left: 40px;
    top: 138px;
    display: flex;
    align-items: flex-start;
    gap: 14px;
  }
  .brand-dot {
    width: 40px; height: 40px;
    border: 1.5px solid var(--ink-soft);
    border-radius: 50%;
    margin-top: 4px;
  }
  .card-back .wordmark .name { font-size: 36px; }
  .card-back .wordmark .trade { font-size: 25px; }
  .campus {
    font-family: "Cormorant Garamond", serif;
    font-style: italic;
    font-size: 12px;
    color: var(--ink-soft);
    margin-top: 4px;
  }
  .campus-address {
    font-family: "Cormorant Garamond", serif;
    font-size: 7px;
    letter-spacing: 0.06em;
    text-transform: uppercase;
    color: var(--ink-soft);
    margin-top: 2px;
  }
  .divider {
    position: absolute;
    left: 336px;
    top: 110px;
    width: 1.5px;
    height: 190px;
    background: var(--rule);
  }
  .contact {
    position: absolute;
    left: 368px;
    top: 112px;
    font-family: "Work Sans", sans-serif;
    color: var(--ink);
  }
  .person-name { font-size: 20px; font-weight: 500; letter-spacing: 0.02em; }
  .person-role { font-size: 14px; color: var(--ink-soft); margin-top: 2px; }
  .address { font-size: 15px; line-height: 1.45; margin-top: 14px; letter-spacing: 0.02em; }
  .lines { list-style: none; margin-top: 10px; }
  .lines li {
    display: flex; align-items: center; gap: 10px;
    font-size: 16px; line-height: 1.5; letter-spacing: 0.03em;
  }
  .lines svg { width: 11px; height: 11px; flex: none; }
</style>
</head>
<body>

  <section class="card card-front" aria-label="Card front">
    <div class="pattern-field" role="img" aria-label="Repeating pattern of outlined figures in gloss black"></div>
    <div class="wordmark">
      <span class="name">BRELLMORE</span>
      <span class="trade">Chiropractic</span>
    </div>
  </section>

  <section class="card card-back" aria-label="Card back">
    <div class="brand">
      <span class="brand-dot"></span>
      <div>
        <div class="wordmark">
          <span class="name">BRELLMORE</span>
          <span class="trade">Chiropractic</span>
        </div>
        <p class="campus">Calderwick Professional Campus</p>
        <p class="campus-address">3815 Pemberly Dr., Suite 240 &nbsp;Flowood, MS 39587</p>
      </div>
    </div>

    <div class="divider"></div>

    <div class="contact">
      <p class="person-name">TOBIAS R VENMARK, D.C.</p>
      <p class="person-role">Director</p>
      <p class="address">426 Larkmoor Dr., Building D.,<br>Madison, MS 39674.</p>
      <ul class="lines">
        <li>
          <svg viewBox="0 0 12 12" aria-hidden="true"><path d="M2.5 1 L4.5 1 L5 3.5 L3.8 4.4 Q4.8 6.8 7.6 8.2 L8.5 7 L11 7.5 L11 9.5 Q10.5 11 9 11 Q2 9.5 1 3 Q1 1.5 2.5 1Z" fill="var(--ink)"/></svg>
          (601)555-0148
        </li>
        <li>
          <svg viewBox="0 0 12 12" aria-hidden="true"><rect x="3" y="1" width="6" height="3" fill="var(--ink)"/><rect x="1" y="4.5" width="10" height="4.5" rx="1" fill="var(--ink)"/><rect x="3" y="8" width="6" height="3" fill="var(--ink)"/></svg>
          (601)555-0173
        </li>
        <li>
          <svg viewBox="0 0 12 12" aria-hidden="true"><circle cx="6" cy="6" r="5" fill="none" stroke="var(--ink)" stroke-width="1"/><ellipse cx="6" cy="6" rx="2.2" ry="5" fill="none" stroke="var(--ink)" stroke-width="1"/><line x1="1" y1="6" x2="11" y2="6" stroke="var(--ink)" stroke-width="1"/></svg>
          www.drbrellmore.example
        </li>
      </ul>
    </div>
  </section>

</body>
</html>
```